Brookvale capital

We lend hard money loans for fixer upper homes and new constructions.Easy Financing on Fix Homes

Target Market(s)

People that need loans & money to buy a Home

Industry/Entity Type

Mortgage Lender

Font styles to use
Serif
Sans Serif

Colors
ffffff
9ccb3b

Requirements
Must have
• Catchy, modern, Clean
Nice to have
• Easy to read

```html
<!DOCTYPE html>
<html lang="en">
<head>
<meta charset="utf-8">
<title>Brookvale capital — Stationery</title>
<link href="https://fonts.googleapis.com/css2?family=Montserrat:wght@700&family=Roboto:wght@400;700&display=swap" rel="stylesheet">
<style>
:root{
  --green:#9ccb3b;
  --green-bright:#7dc242;
  --ink:#1d1d1d;
  --paper:#ffffff;
  --table:#a9a9ae;
  --muted:#555;
}
*{margin:0;padding:0;box-sizing:border-box}
html,body{width:1200px;height:1041px;overflow:hidden}
body{background:var(--table);position:relative;font-family:"Roboto",Arial,sans-serif}
.sheet{position:absolute;overflow:hidden}
.wordmark{position:absolute;font-family:"Montserrat",Arial,sans-serif;font-weight:700;white-space:nowrap;line-height:1.05;text-align:center}
.wordmark span{display:block}
.mark-circle{position:absolute;border-radius:50%;border:2px solid var(--green)}
.wave{position:absolute;left:0;bottom:0;width:100%}

/* folder */
.folder{left:166px;top:77px;width:417px;height:540px;background:var(--ink);border-radius:3px}
.folder-spine{position:absolute;left:26px;top:0;width:2px;height:100%;background:#111}
.folder .mark-circle{left:100px;top:66px;width:216px;height:216px;border-width:3px}
.folder .wordmark{left:0;width:100%;top:438px;font-size:26px;color:#d8d8d8}

/* letterhead */
.letterhead{left:615px;top:95px;width:403px;height:522px;background:var(--paper)}
.letterhead .mark-circle{left:41px;top:27px;width:56px;height:56px}
.letterhead .wordmark{left:19px;width:100px;top:88px;font-size:12px;color:var(--ink)}
.contact{position:absolute;font-size:5px;color:var(--muted);line-height:7px}
.letterhead .contact{left:294px;top:34px}
.contact .addr{border-left:1px solid var(--green);padding-left:4px;margin-bottom:6px}
.contact .row{display:flex;align-items:center;gap:3px}
.contact svg{width:5px;height:5px;fill:var(--green)}

/* envelope front */
.envelope-front{left:132px;top:645px;width:451px;height:196px;background:var(--paper)}
.envelope-front .mark-circle{left:34px;top:19px;width:56px;height:56px}
.envelope-front .wordmark{left:12px;width:100px;top:80px;font-size:12px;color:var(--ink)}
.return-addr{position:absolute;left:35px;top:161px;font-size:5px;line-height:7px;color:var(--muted);text-align:center}

/* envelope back */
.envelope-back{left:615px;top:645px;width:451px;height:196px;background:var(--paper)}
.flap{position:absolute;left:0;top:0;width:100%;height:65px}
.envelope-back .mark-circle{left:212px;top:20px;width:28px;height:28px;border-width:1.5px}

/* business cards */
.card{top:870px;width:166px;height:95px;border-radius:6px}
.card-front{left:418px;background:var(--paper)}
.card-front .mark-circle{left:24px;top:16px;width:36px;height:36px;border-width:1.5px}
.card-front .wordmark{left:6px;width:72px;top:55px;font-size:7px;color:var(--ink)}
.card-divider{position:absolute;left:78px;top:20px;width:1px;height:50px;background:#ddd}
.card-front .contact{left:86px;top:22px;font-size:4px;line-height:5.5px}
.card-name{font-weight:700;color:var(--green-bright);font-size:5px}
.card-back{left:615px;background:var(--ink)}
.card-back .mark-circle{left:61px;top:14px;width:44px;height:44px;border-width:1.5px}
.card-back .wordmark{left:0;width:100%;top:63px;font-size:8px;color:#e0e0e0}
</style>
</head>
<body>

<svg width="0" height="0" style="position:absolute">
  <defs>
    <symbol id="wave" viewBox="0 0 400 30" preserveAspectRatio="none">
      <path d="M0 30 L0 22 C120 12 250 -2 400 8 L400 30 Z" fill="#9ccb3b"/>
      <path d="M0 30 L0 28 C130 18 260 4 400 13 L400 30 Z" fill="#ffffff"/>
      <path d="M120 30 C200 14 300 8 400 17 L400 30 Z" fill="#1d1d1d"/>
    </symbol>
    <symbol id="i-phone" viewBox="0 0 10 10"><path d="M2 1l2 0 1 2-1 1c.6 1.2 1.3 1.9 2.5 2.5l1-1 2 1v2c-4 0-7.5-3.5-7.5-7.5z"/></symbol>
    <symbol id="i-mail" viewBox="0 0 10 10"><path d="M0 2h10v6H0z M0 2l5 3 5-3"/></symbol>
    <symbol id="i-web" viewBox="0 0 10 10"><circle cx="5" cy="5" r="4.5"/></symbol>
  </defs>
</svg>

<section class="sheet folder">
  <div class="folder-spine"></div>
  <div class="mark-circle"></div>
  <div class="wordmark"><span>Brookvale</span><span>capital</span></div>
</section>

<section class="sheet letterhead">
  <div class="mark-circle"></div>
  <div class="wordmark"><span>Brookvale</span><span>capital</span></div>
  <div class="contact">
    <div class="addr">240 Harbor Ave<br>Riverton, NY 10021</div>
    <div class="addr">18 Elm Court Plaza<br>Millbrook, NY 10412</div>
    <div class="row"><svg><use href="#i-phone"/></svg>(555) 014-2290</div>
    <div class="row"><svg><use href="#i-mail"/></svg>info@brookvalecap.com</div>
    <div class="row"><svg><use href="#i-web"/></svg>www.brookvalecap.com</div>
  </div>
  <svg class="wave" height="28"><use href="#wave"/></svg>
</section>

<section class="sheet envelope-front">
  <div class="mark-circle"></div>
  <div class="wordmark"><span>Brookvale</span><span>capital</span></div>
  <div class="return-addr">18 Elm Court Plaza<br>Millbrook, NY 10412</div>
  <svg class="wave" height="28"><use href="#wave"/></svg>
</section>

<section class="sheet envelope-back">
  <svg class="flap" viewBox="0 0 451 65" preserveAspectRatio="none">
    <path d="M0 0 H451 L430 58 Q428 65 420 65 H31 Q23 65 21 58 Z" fill="#1d1d1d"/>
  </svg>
  <div class="mark-circle"></div>
</section>

<section class="sheet card card-front">
  <div class="mark-circle"></div>
  <div class="wordmark"><span>Brookvale</span><span>capital</span></div>
  <div class="card-divider"></div>
  <div class="contact">
    <div class="card-name">JORDAN HALE</div>
    <div style="margin-bottom:3px">General Manager</div>
    <div class="row"><svg><use href="#i-phone"/></svg>(555) 014-2290</div>
    <div class="row"><svg><use href="#i-mail"/></svg>info@brookvalecap.com</div>
    <div class="row" style="margin-bottom:3px"><svg><use href="#i-web"/></svg>www.brookvalecap.com</div>
    <div>18 Elm Court Plaza<br>Millbrook, NY 10412</div>
  </div>
  <svg class="wave" height="14"><use href="#wave"/></svg>
</section>

<section class="sheet card card-back">
  <div class="mark-circle"></div>
  <div class="wordmark"><span>Brookvale</span><span>capital</span></div>
</section>

</body>
</html>
```